Business Card and Stationary Design

After the successful redesign of our logo we are wanting to follow suite and create a new business card and stationary design!

New Logo is attached, information required on the business card should contain a mixture of the following but layout/arrangement is up to the designer.

Happy if the national provider number and abn are on the back, and happy for them to be smaller than the rest.

I am also happy to receive single sided or weird and wonderful designs.

Name
Title
National Provider Number 7291
ABN 53 219 864 317
Level 3, 42 Marlow Street
Kenbrook NSW 2391
Ph: 1300 987 214
Mobile: 0432 785 619
name@ferngatebuild.com.au
www.ferngatebuild.com.au

Target Market(s)

Professionals, Peers, Students, Suppliers...

Industry/Entity Type

Construction

Contact Information for Business Card

Listed in project description

Font styles to use
Other font styles liked:
• Century Gothic

Colors
0455a3
3176b5
ffffff

Requirements
Must have
• Professional Design, same color scheme as our logo
Nice to have
• Something that sets our apart from everyone else would be fantastic, open to size and shape and layout options, as long as they present professionally.
• Open to raised/embossed text, alternative materials, custom sizes, clear material
Should not have
• The color orange

```html
<!DOCTYPE html>
<html lang="en">
<head>
<meta charset="utf-8">
<title>Ferngatebuild Business Card</title>
<link href="https://fonts.googleapis.com/css2?family=Questrial&display=swap" rel="stylesheet">
<style>
  :root {
    --brand-blue: #1f3a9e;
    --accent-blue: #3176b5;
    --card-white: #ffffff;
    --card-shade: #eeeeee;
    --ink: #3a3a3a;
    --ink-soft: #555555;
    --backdrop: #2a2a2a;
  }
  * { box-sizing: border-box; margin: 0; padding: 0; }
  html, body {
    width: 1200px;
    height: 834px;
    overflow: hidden;
    background: var(--backdrop);
    font-family: "Questrial", sans-serif;
  }
  .stage { position: relative; width: 1200px; height: 834px; }
  .card {
    position: absolute;
    width: 520px;
    height: 298px;
    background: linear-gradient(135deg, var(--card-white) 0%, var(--card-shade) 100%);
    box-shadow: 0 8px 24px rgba(0,0,0,0.45);
    overflow: hidden;
  }
  .card-front { left: 70px; top: 110px; }
  .card-back { left: 610px; top: 426px; }

  .wordmark {
    display: flex;
    align-items: center;
    gap: 10px;
    color: var(--brand-blue);
    font-size: 34px;
    letter-spacing: -0.5px;
    white-space: nowrap;
  }
  .wordmark-square {
    width: 22px;
    height: 22px;
    background: var(--brand-blue);
  }
  .card-front .wordmark {
    position: absolute;
    left: 50%;
    top: 50%;
    transform: translate(-50%, -50%);
  }

  .band {
    position: absolute;
    left: 0;
    width: 100%;
    height: 9px;
    background: var(--brand-blue);
  }
  .band-top { top: 0; }
  .band-bottom { bottom: 0; }
  .top-rule {
    position: absolute;
    top: 38px;
    left: 250px;
    right: 0;
    height: 1px;
    background: var(--brand-blue);
  }
  .card-back .wordmark {
    position: absolute;
    left: 28px;
    top: 150px;
    font-size: 27px;
  }
  .wordmark-back .wordmark-square { width: 18px; height: 18px; }

  .details {
    position: absolute;
    left: 292px;
    top: 52px;
    width: 214px;
    color: var(--ink-soft);
    font-size: 11.5px;
    line-height: 1.45;
    white-space: nowrap;
  }
  .person-name { color: var(--ink); font-size: 17px; font-weight: 700; letter-spacing: 0.2px; }
  .person-title { color: var(--brand-blue); font-size: 13px; margin-top: 1px; }
  .name-rule { height: 1px; background: var(--brand-blue); margin: 6px 0 8px; }
  .company-info { margin-bottom: 12px; }
  .contact-line { display: flex; gap: 6px; }
  .contact-key { color: var(--brand-blue); font-weight: 700; width: 12px; }
</style>
</head>
<body>
<main class="stage">
  <section class="card card-front" aria-label="Card front">
    <div class="wordmark">
      <span class="wordmark-square"></span>
      <span class="wordmark-text">ferngatebuild</span>
    </div>
  </section>

  <section class="card card-back" aria-label="Card back">
    <div class="band band-top"></div>
    <div class="top-rule"></div>

    <div class="wordmark wordmark-back">
      <span class="wordmark-square"></span>
      <span class="wordmark-text">ferngatebuild</span>
    </div>

    <div class="details">
      <p class="person-name">Alex Carter</p>
      <p class="person-title">President</p>
      <div class="name-rule"></div>
      <div class="company-info">
        <p>National Provider Number 7291</p>
        <p>ABN 53 219 864 317</p>
        <p>Level 3, 42 Marlow Street</p>
        <p>Kenbrook NSW 2391</p>
      </div>
      <div class="contacts">
        <p class="contact-line"><span class="contact-key">P</span><span>1300 987 214</span></p>
        <p class="contact-line"><span class="contact-key">M</span><span>0432 785 619</span></p>
        <p class="contact-line"><span class="contact-key">E</span><span>name@ferngatebuild.com.au</span></p>
        <p class="contact-line"><span class="contact-key">W</span><span>www.ferngatebuild.com.au</span></p>
      </div>
    </div>

    <div class="band band-bottom"></div>
  </section>
</main>
</body>
</html>
```